Letterhead Design Project

Please see attached logo as well as information below which could be relevant to design. Let me know if you have any questions.

Derek J. Holloman
Estate Planning and Insurance Specialist
Dholloman@brenwickfinancial.com
P: 516-471-2958 F: 516-471-3085
www.brenwickfinancial.com
4300 Maple Ridge Road, Suite 305E
Elmbrook, New York 11804

```html
<!DOCTYPE html>
<html lang="en">
<head>
<meta charset="utf-8">
<title>Brenwick Financial Group Letterhead</title>
<link rel="stylesheet" href="https://fonts.googleapis.com/css2?family=Archivo:wght@500;600;700&family=Cormorant+Garamond:wght@500&display=swap">
<style>
  :root {
    --paper: #ffffff;
    --ink: #111111;
    --navy: #25252d;
    --gold: #cdb57c;
  }
  * { margin: 0; padding: 0; box-sizing: border-box; }
  html, body { width: 848px; height: 1200px; overflow: hidden; background: var(--paper); }
  .sheet { position: relative; width: 848px; height: 1200px; background: var(--paper); font-family: "Archivo", Arial, sans-serif; }

  .brand-top {
    position: absolute; top: 66px; left: 0; width: 848px;
    display: flex; justify-content: center; align-items: center; gap: 14px;
  }
  .brand-top .mark { width: 22px; height: 22px; background: var(--navy); }
  .brand-top .name {
    font-family: "Cormorant Garamond", Georgia, serif; font-weight: 500;
    font-size: 30px; letter-spacing: 3px; color: var(--navy); text-transform: uppercase;
  }

  .sender {
    position: absolute; right: 36px; top: 1055px; text-align: right;
    text-transform: uppercase; color: var(--ink);
  }
  .sender .person { font-weight: 700; font-size: 14.5px; letter-spacing: 0.3px; margin-bottom: 8px; }
  .sender .role, .sender .address { font-weight: 600; font-size: 12px; letter-spacing: 0.2px; line-height: 20px; }

  .rule { position: absolute; left: 352px; top: 1128px; width: 460px; height: 3px; background: var(--gold); }

  .footer { position: absolute; left: 0; top: 1138px; width: 848px; height: 62px; background: var(--navy); color: var(--gold); }
  .footer .brand { position: absolute; left: 36px; top: 20px; display: flex; align-items: center; gap: 8px; }
  .footer .brand .mark { width: 14px; height: 14px; background: var(--gold); }
  .footer .brand .name { font-family: "Cormorant Garamond", Georgia, serif; font-weight: 500; font-size: 15px; letter-spacing: 0.6px; text-transform: uppercase; white-space: nowrap; }
  .footer .phones { position: absolute; left: 313px; top: 42px; font-size: 10.5px; font-weight: 600; letter-spacing: 0.4px; white-space: nowrap; }
  .footer .online { position: absolute; right: 42px; top: 13px; text-align: right; font-size: 10.5px; font-weight: 600; letter-spacing: 0.3px; line-height: 22px; text-transform: uppercase; white-space: nowrap; }
</style>
</head>
<body>
<div class="sheet">
  <header class="brand-top">
    <span class="mark"></span>
    <span class="name">Brenwick Financial Group</span>
  </header>

  <section class="sender">
    <p class="person">Derek J. Holloman</p>
    <p class="role">Estate Planning and Insurance Specialist</p>
    <p class="address">4300 Maple Ridge Road, Suite 305E Elmbrook, New York 11804</p>
  </section>

  <div class="rule"></div>

  <footer class="footer">
    <div class="brand">
      <span class="mark"></span>
      <span class="name">Brenwick Financial Group</span>
    </div>
    <p class="phones">PHONE : 555-471-2958 &nbsp;F: 555-471-3085</p>
    <div class="online">
      <p>www.brenwickfinancial.com</p>
      <p>Dholloman@brenwickfinancial.com</p>
    </div>
  </footer>
</div>
</body>
</html>
```